Franchise Vacation Rental Company Website

We are looking for fresh, new and creative design ideas to help enhance this site. We are a vacation rental company that is starting a new franchise business. This will be our home franchise page, and will need to appeal to franchise candidates as well as travelers looking for vacation homes in our current locations.

Business

```html
<!DOCTYPE html>
<html lang="en">
<head>
<meta charset="utf-8">
<title>BrightHaven – Vacation Rentals</title>
<link rel="stylesheet" href="https://fonts.googleapis.com/css2?family=Open+Sans:ital,wght@0,400;0,600;0,700;1,600&display=swap">
<style>
:root{
  --page:#141414;
  --panel:#1f1f1f;
  --band:#3a3a3c;
  --green:#a8c82e;
  --text:#e6e6e6;
  --muted:#9a9a9a;
  --white:#ffffff;
  --icon-grey:#6a6a6a;
}
*{box-sizing:border-box;margin:0;padding:0}
html,body{width:748px;height:1200px;overflow:hidden;background:var(--page)}
body{font-family:"Open Sans",Arial,sans-serif;color:var(--text);position:relative}
.wrap{position:absolute;left:100px;width:548px}

/* hero */
.hero{position:absolute;top:0;left:0;width:748px;height:196px}
.hero-photo{position:absolute;inset:0;
  background:linear-gradient(180deg,#7fbde4 0%,#a9d9ef 35%,#3bb5c4 55%,#d6cbb0 80%,#c9b994 100%)}
.topnav{position:absolute;top:22px;left:100px;width:548px;height:30px;background:rgba(10,10,10,.88);
  border:1px solid var(--green);display:flex;align-items:center;justify-content:space-between;padding:0 12px}
.brand{font-size:19px;font-weight:400;color:var(--white);display:flex;align-items:center;gap:5px}
.brand-dot{width:9px;height:9px;border-radius:50%;background:var(--green)}
.topnav ul{list-style:none;display:flex;font-size:8px;color:#ddd}
.topnav li{padding:0 5px;border-left:1px solid #888}
.topnav li:first-child{border-left:0}

/* contact band */
.contact-band{position:absolute;top:196px;left:0;width:748px;height:62px;background:var(--band);border-bottom:2px solid var(--green)}
.contact-info{position:absolute;left:100px;top:16px;font-size:10px;font-weight:600;line-height:14px;color:#e2e2e2}
.search{position:absolute;left:370px;top:16px;width:212px;height:22px;background:var(--white)}
.search-btn{position:absolute;left:590px;top:10px;width:56px;height:40px}

/* destinations */
.destinations{top:276px;display:flex;justify-content:space-between}
.dest{width:112px}
.dest-img{height:86px}
.dest-name{font-size:8px;font-weight:700;color:var(--green);text-align:right;margin-top:2px;text-transform:uppercase}
.img-roma{background:linear-gradient(160deg,#d99a55,#7a5a3e 60%,#4f4a3e)}
.img-venice{background:linear-gradient(160deg,#e2c4a0,#b7735a 55%,#e5dbc9)}
.img-miami{background:linear-gradient(180deg,#5aa7dc,#c9e4f2 50%,#2eb4c4)}
.img-bora{background:linear-gradient(180deg,#6eb0e2,#e8eef2 40%,#a88e6e 75%,#d8c8a8)}

/* main */
.main{top:390px;height:400px;border-top:2px solid var(--green)}
.articles{position:absolute;left:0;top:14px;width:354px}
.article h2{font-size:12px;font-weight:700;color:var(--green);margin-bottom:8px}
.article p{font-size:7.2px;line-height:10.4px;text-align:justify;color:#ddd;height:146px;overflow:hidden}
.article+.article{margin-top:18px}
.divider{position:absolute;left:370px;top:0;width:1px;height:398px;background:var(--green)}
.sidebar{position:absolute;left:382px;top:12px;width:166px}
.map{height:112px;border:2px solid #ddd;background:linear-gradient(150deg,#b9d8ee,#e4e0cf 45%,#a9cfe8)}
.find{display:flex;align-items:center;gap:4px;margin:6px 0 0 18px;font-size:9px;font-weight:700;color:var(--white);text-transform:uppercase}
.perks{list-style:none;margin:22px 0 0 30px}
.perks li{display:flex;align-items:center;gap:8px;height:44px;font-size:7.5px;font-weight:600;font-style:italic;color:var(--white)}
.signup{display:flex;gap:6px;margin-top:60px}
.signup-field{width:90px;height:16px;background:var(--white)}
.signup-btn{width:58px;height:16px;background:var(--green);color:#222;font-size:7px;font-weight:700;text-align:center;line-height:16px}

/* featured */
.strip{position:absolute;top:796px;left:100px;width:548px;height:10px;background:var(--white)}
.featured{top:812px;height:180px;background:var(--panel);display:flex;justify-content:space-between;padding:12px 20px}
.card{width:110px}
.card-img{height:86px}
.card h3{font-size:8px;font-weight:700;color:var(--white);margin:10px 0 14px}
.card p{font-size:5.5px;line-height:8px;color:var(--muted)}

/* footer nav */
.footnav{position:absolute;top:1004px;left:0;width:748px;height:24px;border-top:2px solid var(--green);border-bottom:2px solid var(--green);background:#0c0c0c}
.footnav ul{list-style:none;position:absolute;left:100px;top:3px;display:flex;gap:6px}
.footnav li{display:flex;align-items:center;gap:4px;font-size:6.5px;color:#ddd;width:70px;justify-content:space-between}
.chev{width:8px;height:14px}
.social{position:absolute;right:100px;top:5px;display:flex;gap:4px}
.social span{width:11px;height:11px;border-radius:50%;background:var(--icon-grey)}

/* footer */
.footer{top:1044px;display:flex;justify-content:space-between}
.footer-col{width:124px}
.footer-col h4{font-size:11px;font-weight:700;color:var(--green);margin-bottom:3px}
.footer-col p{font-size:7px;line-height:9.6px;text-align:justify;color:#ddd;height:58px;overflow:hidden}
.base{position:absolute;top:1150px;left:0;width:748px;height:50px;border-top:2px solid var(--green);background:#101010}
</style>
</head>
<body>

<header class="hero">
  <div class="hero-photo" role="img" aria-label="Photo of a couple relaxing in beach chairs on a tropical turquoise beach"></div>
  <nav class="topnav">
    <div class="brand">BrightHaven <span class="brand-dot"></span></div>
    <ul>
      <li>Home</li><li>Your Property</li><li>Contact BrightHaven</li><li>Franchise</li><li>Philosophy</li><li>News</li>
    </ul>
  </nav>
</header>

<section class="contact-band">
  <div class="contact-info">1.800.555.0147<br>info@brighthaven-stays.com</div>
  <div class="search"></div>
  <svg class="search-btn" viewBox="0 0 56 40"><polygon points="8,1 55,1 55,39 1,39" fill="none" stroke="#a8c82e" stroke-width="1.5"/><circle cx="31" cy="18" r="7" fill="none" stroke="#a8c82e" stroke-width="2"/><line x1="26" y1="23" x2="20" y2="30" stroke="#a8c82e" stroke-width="2.5"/></svg>
</section>

<section class="wrap destinations">
  <div class="dest"><div class="dest-img img-roma" role="img" aria-label="Narrow sunlit street in Rome"></div><div class="dest-name">Roma</div></div>
  <div class="dest"><div class="dest-img img-venice" role="img" aria-label="Tourists in a gondola in Venice"></div><div class="dest-name">Venecia</div></div>
  <div class="dest"><div class="dest-img img-miami" role="img" aria-label="Cruise ship at sea off Miami"></div><div class="dest-name">Miami</div></div>
  <div class="dest"><div class="dest-img img-bora" role="img" aria-label="Beach chairs on the sand in Bora Bora"></div><div class="dest-name">Bora Bora</div></div>
</section>

<main class="wrap main">
  <div class="articles">
    <article class="article">
      <h2>Ready to Discover</h2>
      <p>Sed ut perspiciatis unde omnis iste natus error sit voluptatem accusantium doloremque laudantium, totam rem aperiam, eaque ipsa quae ab illo inventore veritatis et quasi architecto beatae vitae dicta sunt explicabo. Nemo enim ipsam voluptatem quia voluptas sit aspernatur aut odit aut fugit, sed quia consequuntur magni dolores eos qui ratione voluptatem sequi nesciunt. Sed ut perspiciatis unde omnis iste natus error sit voluptatem accusantium doloremque laudantium, totam rem aperiam, eaque ipsa quae ab illo inventore veritatis et quasi architecto beatae vitae dicta sunt explicabo. Nemo enim ipsam voluptatem quia voluptas sit aspernatur aut odit aut fugit. Totam rem aperiam, eaque ipsa quae ab illo inventore veritatis et quasi architecto beatae vitae dicta sunt explicabo. Nemo enim ipsam voluptatem quia voluptas sit aspernatur aut odit aut fugit, sed quia consequuntur magni dolores eos qui ratione voluptatem sequi nesciunt. Neque porro quisquam est, qui dolorem ipsum quia dolor sit amet, consectetur, adipisci velit, sed quia non numquam eius modi tempora incidunt ut labore et dolore magnam aliquam quaerat voluptatem. Ut enim ad minima veniam, quis nostrum exercitationem ullam corporis suscipit laboriosam.</p>
    </article>
    <article class="article">
      <h2>Ready to Discover</h2>
      <p>Sed ut perspiciatis unde omnis iste natus error sit voluptatem accusantium doloremque laudantium, totam rem aperiam, eaque ipsa quae ab illo inventore veritatis et quasi architecto beatae vitae dicta sunt explicabo. Nemo enim ipsam voluptatem quia voluptas sit aspernatur aut odit aut fugit, sed quia consequuntur magni dolores eos qui ratione voluptatem sequi nesciunt. Sed ut perspiciatis unde omnis iste natus error sit voluptatem accusantium doloremque laudantium, totam rem aperiam, eaque ipsa quae ab illo inventore veritatis et quasi architecto beatae vitae dicta sunt explicabo. Nemo enim ipsam voluptatem quia voluptas sit aspernatur aut odit aut fugit. Totam rem aperiam, eaque ipsa quae ab illo inventore veritatis et quasi architecto beatae vitae dicta sunt explicabo. Nemo enim ipsam voluptatem quia voluptas sit aspernatur aut odit aut fugit, sed quia consequuntur magni dolores eos qui ratione voluptatem sequi nesciunt. Neque porro quisquam est, qui dolorem ipsum quia dolor sit amet, consectetur, adipisci velit, sed quia non numquam eius modi tempora incidunt ut labore et dolore magnam aliquam quaerat voluptatem. Ut enim ad minima veniam, quis nostrum exercitationem ullam corporis suscipit laboriosam.</p>
    </article>
  </div>
  <div class="divider"></div>
  <aside class="sidebar">
    <div class="map" role="img" aria-label="World map showing rental locations"></div>
    <div class="find">
      <svg width="9" height="12" viewBox="0 0 9 12"><path d="M4.5 11.5 C1 7 0.5 5.5 0.5 4.5 a4 4 0 0 1 8 0 C8.5 5.5 8 7 4.5 11.5Z" fill="none" stroke="#a8c82e" stroke-width="1.2"/></svg>
      Find your bright haven!
    </div>
    <ul class="perks">
      <li><svg width="14" height="18" viewBox="0 0 14 18"><path d="M7 17 C2 10 1 8 1 6.5 a6 6 0 0 1 12 0 C13 8 12 10 7 17Z" fill="none" stroke="#fff" stroke-width="1.5"/></svg>Know of a Bright Haven?</li>
      <li><svg width="16" height="14" viewBox="0 0 16 14"><circle cx="5" cy="3.5" r="2.6" fill="#fff"/><circle cx="11" cy="4.5" r="2.2" fill="#fff"/><path d="M0.5 13 a4.5 5 0 0 1 9 0Z M8 13 a3.5 4 0 0 1 7.5 0Z" fill="#fff"/></svg>Stay travels free!</li>
      <li><svg width="15" height="15" viewBox="0 0 15 15"><circle cx="7.5" cy="7.5" r="6.5" fill="none" stroke="#fff" stroke-width="1.4"/><path d="M7.5 3.5 V7.5 H10.5" fill="none" stroke="#fff" stroke-width="1.4"/></svg>Last Minute Deals!</li>
    </ul>
    <div class="signup"><div class="signup-field"></div><div class="signup-btn">Sign me up!</div></div>
  </aside>
</main>

<div class="strip"></div>

<section class="wrap featured">
  <div class="card"><div class="card-img img-roma" role="img" aria-label="Narrow sunlit street in Rome"></div><h3>Roma</h3><p>Lorem ipsum dolor sit<br>Sed ut perspiciatis<br>In rhoncus felis<br>Mauris eget orci</p></div>
  <div class="card"><div class="card-img img-venice" role="img" aria-label="Tourists in a gondola in Venice"></div><h3>Venecia</h3><p>Lorem ipsum dolor sit<br>Sed ut perspiciatis<br>In rhoncus felis<br>Mauris eget orci</p></div>
  <div class="card"><div class="card-img img-miami" role="img" aria-label="Cruise ship at sea off Miami"></div><h3>Miami</h3><p>Lorem ipsum dolor sit<br>Sed ut perspiciatis<br>In rhoncus felis<br>Mauris eget orci</p></div>
  <div class="card"><div class="card-img img-bora" role="img" aria-label="Beach chairs on the sand in Bora Bora"></div><h3>Bora Bora</h3><p>Lorem ipsum dolor sit<br>Sed ut perspiciatis<br>In rhoncus felis<br>Mauris eget orci</p></div>
</section>

<nav class="footnav">
  <ul>
    <li>Franchise<svg class="chev" viewBox="0 0 8 14"><polygon points="0,0 4,0 8,7 4,14 0,14 4,7" fill="#a8c82e"/></svg></li>
    <li>Philosophy<svg class="chev" viewBox="0 0 8 14"><polygon points="0,0 4,0 8,7 4,14 0,14 4,7" fill="#a8c82e"/></svg></li>
    <li>Your Ad<svg class="chev" viewBox="0 0 8 14"><polygon points="0,0 4,0 8,7 4,14 0,14 4,7" fill="#a8c82e"/></svg></li>
    <li>Contact Us<svg class="chev" viewBox="0 0 8 14"><polygon points="0,0 4,0 8,7 4,14 0,14 4,7" fill="#a8c82e"/></svg></li>
    <li>Site Map<svg class="chev" viewBox="0 0 8 14"><polygon points="0,0 4,0 8,7 4,14 0,14 4,7" fill="#a8c82e"/></svg></li>
    <li>Policy<svg class="chev" viewBox="0 0 8 14"><polygon points="0,0 4,0 8,7 4,14 0,14 4,7" fill="#a8c82e"/></svg></li>
  </ul>
  <div class="social"><span></span><span></span><span></span><span></span></div>
</nav>

<footer class="wrap footer">
  <div class="footer-col"><h4>BrightHaven</h4><p>Sed ut perspiciatis unde omnis iste natus error sit voluptatem accusantium doloremque laudantium, totam rem aperiam, eaque ipsa quae ab illo inventore veritatis et quasi architecto beatae.</p></div>
  <div class="footer-col"><h4>Contact Us</h4><p>Sed ut perspiciatis unde omnis iste natus error sit voluptatem accusantium doloremque laudantium, totam rem aperiam, eaque ipsa quae ab illo inventore veritatis et quasi architecto beatae.</p></div>
  <div class="footer-col"><h4>Franchise</h4><p>Sed ut perspiciatis unde omnis iste natus error sit voluptatem accusantium doloremque laudantium, totam rem aperiam, eaque ipsa quae ab illo inventore veritatis et quasi architecto beatae.</p></div>
</footer>

<div class="base"></div>

</body>
</html>
```